Re-design of website

I have an existing website that I would like to improve. The functionality will remain the same but the overall look will need to be changed. I have some ideas of what i would like included and am also in need of someone else to input their own creative ideas. I am on a tight deadline to get these improvements made as I have many people being directed to the site via our advertising campaigns that are in full swing late next week. Thanks
Target Market(s)
The website provides a virtual space for families to learn more about our learning program which we operate out of Dubai and will soon spread to the other Emirates. The families are generally between 25-50 year old parents with children up to the age of 6. They are local Emirati's as well as expats.
Look and feel

```html
<!DOCTYPE html>
<html lang="en">
<head>
<meta charset="utf-8">
<title>Little Sprouts – Learning Program</title>
<link rel="stylesheet" href="https://fonts.googleapis.com/css2?family=Oswald:wght@600&family=Cinzel:wght@400;700&family=Didact+Gothic&family=Arimo:wght@400;700&display=swap">
<style>
:root{
  --navy:#17427e;
  --navy-deep:#133a6c;
  --green:#5f7f0c;
  --leaf:#6d9a15;
  --ink:#111;
  --body:#555;
  --panel:#ebebeb;
  --rule:#333;
  --olive-rule:#8aa04a;
  --blush:#e8a9a9;
}
*{margin:0;padding:0;box-sizing:border-box}
html,body{width:1200px;height:2350px;overflow:hidden;background:#fff}
body{position:relative;font-family:"Arimo",Arial,sans-serif;color:var(--ink)}
.abs{position:absolute}

/* hero */
.hero-photo{left:0;top:0;width:1200px;height:611px;
  background:radial-gradient(ellipse at 30% 20%,#8b7a45 0%,#4a4f2a 35%,#2b3320 65%,#1c2416 100%)}
.brand{left:470px;top:170px;display:flex;align-items:center;gap:8px;
  font-family:"Arimo",Arial,sans-serif;font-weight:700;font-size:17px;color:#fff}
.brand-dot{width:18px;height:18px;border-radius:50%;background:#fff}
.nav{left:121px;top:210px;width:735px;height:122px;background:#fff;border-radius:10px 0 0 10px;
  display:flex;align-items:center;padding-left:36px}
.nav a{font-size:13.5px;font-weight:700;color:#222;text-decoration:none;margin-right:25px}
.nav .home{display:flex;flex-direction:column;align-items:center;margin-right:24px}
.nav .home svg{margin-bottom:2px}
.search{left:856px;top:210px;width:196px;height:122px;background:var(--navy-deep);border-radius:0 10px 10px 0;
  display:flex;align-items:center;justify-content:center}
.tagline-band{left:0;top:611px;width:1200px;height:74px;background:var(--navy);border-bottom:2px solid #2d5aa0}
.tagline{left:240px;top:640px;font-size:13.5px;font-weight:700;color:#fff}
.social{top:632px;width:30px;height:30px;border-radius:50%;background:#fff}

/* section headings */
.rule{height:1px;background:var(--rule)}
.rule-olive{height:1px;background:var(--olive-rule)}
.section-title{font-family:"Oswald",sans-serif;font-weight:600;font-size:37px;color:var(--navy);letter-spacing:.2px}
.subhead{font-weight:700;font-size:23px;color:var(--ink);line-height:1.15}

/* articles */
.corner{width:34px;height:34px}
.corner-tl{border-top:3px solid var(--navy);border-left:3px solid var(--navy)}
.corner-br{border-bottom:3px solid #222;border-right:3px solid #222}
.article-title{font-family:"Cinzel",serif;font-weight:400;font-size:21px;color:var(--green);letter-spacing:.5px}
.article-body{font-family:"Didact Gothic",sans-serif;font-size:12.6px;line-height:16.6px;color:var(--body)}
.read-more{font-family:"Cinzel",serif;font-weight:700;font-size:10.5px;color:var(--navy);letter-spacing:.3px}

.plain-list{font-family:"Didact Gothic",sans-serif;font-size:14px;line-height:16.5px;color:#222;list-style:none}
.price-copy{font-family:"Didact Gothic",sans-serif;font-size:14.6px;line-height:17px;color:#222}

/* testimonial */
.testimonial{left:143px;top:1921px;width:919px;height:335px;background:var(--panel);border-top:1.5px solid var(--rule)}
.testimonial-title{font-weight:700;font-size:22px;color:var(--green)}
.testimonial-body{font-family:"Didact Gothic",sans-serif;font-size:14px;line-height:17.2px;color:#333}

/* footer */
.footer-text{left:445px;top:2304px;width:343px;text-align:center;font-size:9px;letter-spacing:1.6px;color:#222}
</style>
</head>
<body>

<!-- hero -->
<div class="abs hero-photo" role="img" aria-label="Photo of a young child in a hat and coat holding a butterfly in an autumn forest"></div>
<div class="abs brand"><span class="brand-dot"></span>Little Sprouts</div>

<nav class="abs nav">
  <a class="home" href="#"><svg width="18" height="16" viewBox="0 0 18 16"><path d="M9 1 1 8h2.5v7h4v-4h3v4h4V8H17z" fill="#17427e"/></svg>HOME</a>
  <a href="#">OURMETHOD</a>
  <a href="#">THE PROGRAM</a>
  <a href="#">MEDIA</a>
  <a href="#">LOCATIONS</a>
  <a href="#">ABOUT US</a>
  <a href="#">CONTACT US</a>
</nav>
<div class="abs search">
  <svg width="50" height="50" viewBox="0 0 50 50"><circle cx="30" cy="19" r="13" fill="none" stroke="#fff" stroke-width="4"/><line x1="21" y1="28" x2="7" y2="44" stroke="#fff" stroke-width="5" stroke-linecap="round"/></svg>
</div>

<div class="abs tagline-band"></div>
<p class="abs tagline">our philosophy and curriculum supports like-minded parents who want happiness for their children</p>
<span class="abs social" style="left:925px"></span>
<span class="abs social" style="left:967px"></span>
<span class="abs social" style="left:1011px"></span>

<!-- first recentes -->
<div class="abs rule" style="left:402px;top:799px;width:143px"></div>
<div class="abs rule" style="left:588px;top:799px;width:155px"></div>
<svg class="abs" style="left:562px;top:780px" width="20" height="36" viewBox="0 0 20 36"><path d="M12 2C4 6 2 16 8 22c-2 4-3 8-5 12 4-4 6-8 7-12 7-4 7-14 2-20z" fill="#6d9a15"/></svg>
<h2 class="abs section-title" style="left:0;width:1200px;text-align:center;top:820px;padding-right:20px">FIRST RECENTES</h2>

<span class="abs corner corner-tl" style="left:202px;top:926px"></span>
<div class="abs" style="left:215px;top:940px;width:161px;height:160px;background:linear-gradient(135deg,#3a3a3a,#0a0a0a)" role="img" aria-label="Black and white portrait of two people in profile"></div>
<span class="abs corner corner-br" style="left:354px;top:1080px"></span>
<h3 class="abs article-title" style="left:407px;top:922px">DUMMY ADDRESS</h3>
<p class="abs article-body" style="left:398px;top:983px;width:655px">Halvey is NOT directly affiliated with the Quorvadial project. He is an independent support consultant for Quorvadial (and voice services in general to some degree). More importantly he is a great person and quite possibly greatest consultant there is out there, anywhere.Halvey is NOT directly affiliated with the Quorvadial project. He is an independent support consultant for Quorvadial (and voice services in general to some degree). More importantly he is a great person and quite possibly greatest consultant there is out there, anywhere..</p>
<a class="abs read-more" style="left:964px;top:1103px">READ MORE</a>

<!-- about -->
<div class="abs rule" style="left:133px;top:1219px;width:256px"></div>
<div class="abs rule" style="left:885px;top:1219px;width:183px"></div>
<svg class="abs" style="left:407px;top:1182px" width="48" height="48" viewBox="0 0 48 48"><circle cx="24" cy="24" r="24" fill="#6d9a15"/><path d="M10 22 24 15l14 7-14 7z" fill="#fff"/><path d="M16 25v6c4 4 12 4 16 0v-6l-8 4z" fill="#fff"/></svg>
<h2 class="abs subhead" style="left:492px;top:1198px">ABOUT MY HISTORY AND PRICES</h2>

<h3 class="abs subhead" style="left:270px;top:1278px;width:330px">MY CLIENTS ARE LOCATED EVERYWHERE</h3>
<div class="abs" style="left:190px;top:1343px;width:114px;height:91px;background:linear-gradient(180deg,#222 60%,#fff)" role="img" aria-label="World map with client locations highlighted"></div>
<ul class="abs plain-list" style="left:321px;top:1340px">
  <li>United States</li><li>Manila (Philippines)</li><li>Canada</li><li>India</li>
</ul>

<svg class="abs" style="left:634px;top:1268px" width="46" height="46" viewBox="0 0 46 46"><circle cx="23" cy="23" r="23" fill="#5f7f0c"/><text x="23" y="32" text-anchor="middle" font-family="Arimo,Arial,sans-serif" font-weight="700" font-size="26" fill="#fff">$</text></svg>
<h3 class="abs subhead" style="left:702px;top:1281px">HOW MUCH DO I CHARGE?</h3>
<p class="abs price-copy" style="left:645px;top:1340px;width:440px">I get the majority of my work through referrals, and I have references available at your request. The rest of my business comes from this short letter and its associated advertisement on Zentrovex.</p>

<!-- third recentes -->
<div class="abs rule-olive" style="left:276px;top:1504px;width:686px"></div>
<div class="abs rule-olive" style="left:276px;top:1619px;width:686px"></div>
<svg class="abs" style="left:424px;top:1528px" width="68" height="68" viewBox="0 0 68 68"><circle cx="34" cy="36" r="23" fill="none" stroke="#222" stroke-width="6"/><path d="M34 22v15l9 6" fill="none" stroke="#222" stroke-width="4" stroke-linecap="round"/><circle cx="14" cy="12" r="9" fill="#222"/><circle cx="54" cy="12" r="9" fill="#222"/><path d="M20 56 14 64M48 56l6 8" stroke="#222" stroke-width="5" stroke-linecap="round"/></svg>
<h2 class="abs section-title" style="left:520px;top:1537px">THIRD RECENTES</h2>

<span class="abs corner corner-tl" style="left:224px;top:1687px"></span>
<div class="abs" style="left:232px;top:1695px;width:164px;height:163px;background:linear-gradient(160deg,#6b5a2e,#3b3220 55%,#b0782a)" role="img" aria-label="Photo of a child in a red hat in autumn leaves"></div>
<span class="abs corner corner-br" style="left:372px;top:1833px"></span>
<h3 class="abs article-title" style="left:415px;top:1678px">ANY DUMMY DATA</h3>
<p class="abs article-body" style="left:415px;top:1735px;width:652px">Halvey is NOT directly affiliated with the Quorvadial project. He is an independent support consultant for Quorvadial (and voice services in general to some degree). More importantly he is a great person and quite possibly greatest consultant there is out there, anywhere.Halvey is NOT directly affiliated with the Quorvadial project. He is an independent support consultant for Quorvadial (and voice services in general to some degree). More importantly he is a great person and quite possibly greatest consultant there is out there, anywhere..</p>
<a class="abs read-more" style="left:982px;top:1857px">READ MORE</a>

<!-- testimonial -->
<section class="abs testimonial"></section>
<svg class="abs" style="left:210px;top:1960px" width="58" height="58" viewBox="0 0 58 58"><circle cx="29" cy="29" r="29" fill="#17427e"/><path d="M16 29l9 10 18-20" fill="none" stroke="#fff" stroke-width="6" stroke-linecap="round" stroke-linejoin="round"/></svg>
<h3 class="abs testimonial-title" style="left:310px;top:1988px">AM I ANY GOOD AT THIS?</h3>
<div class="abs" style="left:251px;top:2051px;width:106px;height:107px;border:2px solid #4a72b8;background:linear-gradient(150deg,#6b4a2a,#2a1a10)" role="img" aria-label="Portrait of a young girl"></div>
<p class="abs testimonial-body" style="left:405px;top:2051px;width:640px">Yes. I wasn't always, however. I didn't know Quorvadial existed until the call center I was working at, one with a really expensive proprietary system (think six-figures expensive) broke. The sales floor needed something up and live quickly. Agents who depended upon the commissions generated by the broken system were screaming. A few were literally crying.Yes. I wasn't always, however. I didn't know Quorvadial existed until the call center I was working at,by the broken system were screaming. A few were literally crying..</p>

<!-- footer -->
<div class="abs rule" style="left:445px;top:2291px;width:343px"></div>
<p class="abs footer-text">ALL COPYRIGHTS RESEVED BY YOUR COMPANY</p>
<div class="abs" style="left:445px;top:2327px;width:343px;height:1px;background:var(--blush)"></div>

</body>
</html>
```